Business Card Design - Law Firm

We are a boutique law firm located near the beach in Manly, Australia. We have recently had a new logo designed and are revamping our business cards with the new logo.

We have recently had a business card design done for us but are not entirely happy with it. We are looking for something modern, simplistic but striking. We would like to see multiple designs.

We have attached a word document which includes our new logo and the current business card design which we are looking at moving away from.

We would like the business cards to be double sided. We would like the design to include something which we can print in gloss colour when we send it to the business card printers.

```html
<!DOCTYPE html>
<html lang="en">
<head>
<meta charset="utf-8">
<title>Harlow &amp; Partners Lawyers – Business Card</title>
<link rel="stylesheet" href="https://fonts.googleapis.com/css2?family=Lato:wght@400;700&display=swap">
<style>
  :root {
    --stage: #1d1d20;
    --card-light: #ffffff;
    --card-dark: #0e0f13;
    --brand-blue: #4f5fa8;
    --ink: #3a3a3a;
    --ink-dark: #1e1e1e;
    --paper-white: #ffffff;
  }
  * { box-sizing: border-box; margin: 0; padding: 0; }
  html, body {
    width: 1200px; height: 800px; overflow: hidden;
    background: var(--stage);
    font-family: "Lato", sans-serif;
  }
  .canvas { position: relative; width: 1200px; height: 800px; }
  .card {
    position: absolute; left: 347px; width: 513px; height: 293px;
    border-radius: 18px; overflow: hidden;
  }
  .card--front { top: 66px; background: var(--card-light); }
  .card--back { top: 434px; background: var(--card-dark); }

  .firm-mark {
    position: absolute; display: flex; flex-direction: column; align-items: center;
    text-align: center; font-weight: 700; white-space: nowrap;
  }
  .firm-mark__dot { border-radius: 50%; background: var(--brand-blue); flex: none; }
  .firm-mark__name { display: block; line-height: 1.25; }

  .card--front .firm-mark {
    left: 268px; width: 224px; top: 22px;
    color: var(--ink-dark); font-size: 17px; letter-spacing: 1.6px;
  }
  .card--front .firm-mark__dot { width: 76px; height: 76px; margin-bottom: 16px; }

  .person { position: absolute; left: 21px; top: 141px; }
  .person__name { color: var(--brand-blue); font-weight: 700; font-size: 26px; letter-spacing: -0.3px; line-height: 1; }
  .person__role { color: var(--ink-dark); font-size: 14px; margin-top: 6px; }

  .divider {
    position: absolute; left: 19px; right: 19px; top: 194px;
    height: 1px; background: var(--brand-blue);
  }
  .contacts { position: absolute; left: 21px; top: 203px; list-style: none; }
  .contacts__item {
    display: flex; align-items: center; gap: 8px; height: 22px;
    color: var(--ink); font-size: 14px;
  }
  .contacts__icon { width: 13px; height: 13px; flex: none; }
  .address {
    position: absolute; right: 21px; top: 216px; text-align: right;
    color: var(--ink); font-size: 14px; line-height: 20px; font-style: normal;
  }

  .card--back .firm-mark {
    left: 0; right: 0; top: 56px;
    color: var(--paper-white); font-size: 24px; letter-spacing: 2.5px;
  }
  .card--back .firm-mark__dot { width: 112px; height: 112px; margin-bottom: 22px; }
</style>
</head>
<body>
<main class="canvas">
  <section class="card card--front" aria-label="Business card front">
    <div class="firm-mark">
      <span class="firm-mark__dot"></span>
      <span class="firm-mark__name">Harlow &amp; Partners<br>Lawyers</span>
    </div>

    <div class="person">
      <h1 class="person__name">Nina Calloway</h1>
      <p class="person__role">Practice Manager</p>
    </div>

    <div class="divider"></div>

    <ul class="contacts">
      <li class="contacts__item">
        <svg class="contacts__icon" viewBox="0 0 16 16" aria-hidden="true">
          <path fill="#4f5fa8" d="M1 5c0-2 3-3 7-3s7 1 7 3v1h-3V4.5C10.5 4 5.5 4 4 4.5V6H1z"/>
          <rect x="2" y="7" width="12" height="8" rx="1" fill="#4f5fa8"/>
          <circle cx="8" cy="11" r="2" fill="#fff"/>
        </svg>
        <span>(02) 9410 3786</span>
      </li>
      <li class="contacts__item">
        <svg class="contacts__icon" viewBox="0 0 16 16" aria-hidden="true">
          <rect x="1" y="3" width="14" height="10" fill="#4f5fa8"/>
          <path d="M1 3l7 6 7-6M1 13l5-5M15 13l-5-5" stroke="#fff" stroke-width="1.2" fill="none"/>
        </svg>
        <span>nina.calloway@harbourlegal.com.au</span>
      </li>
      <li class="contacts__item">
        <svg class="contacts__icon" viewBox="0 0 16 16" aria-hidden="true">
          <g fill="none" stroke="#4f5fa8" stroke-width="1.1">
            <circle cx="8" cy="8" r="6.5"/>
            <ellipse cx="8" cy="8" rx="3" ry="6.5"/>
            <path d="M1.5 8h13M2.5 5h11M2.5 11h11M8 1.5v13"/>
          </g>
        </svg>
        <span>www.harlowpartners.com.au</span>
      </li>
    </ul>

    <address class="address">
      Suite 3, 14 Kestrel Lane<br>
      BAYVIEW NSW 2104
    </address>
  </section>

  <section class="card card--back" aria-label="Business card back">
    <div class="firm-mark">
      <span class="firm-mark__dot"></span>
      <span class="firm-mark__name">Harlow &amp; Partners<br>Lawyers</span>
    </div>
  </section>
</main>
</body>
</html>
```